BRACKENRIDGE BUILDERS B-Card

I currently have a b-card design but will be removing the image (tree) from the logo and have text only.
I want the card to be classy and strong within the building and construction industry.
I will be using Spot UV on the cards as per the attached examples. I will also send through some sketched ideas that I have in mind.
The color blue is similar to the image (No. 6) attached images

Target Market(s)

middle to maturre aged.
Home Owners / Renovators and Builders

Industry/Entity Type

Construction

Contact Information for Business Card

BRACKENRIDGE BUILDERS
Name: Dermot Quaile
Title: Project Manager
Mobile: 0412 537 804
Office: (08) 9173 5842
Address: 17C Pellworth Avenue, Malaga WA 6090
Email: info@brackenridgebuild.com.au
PO Box: 3817 Malaga WA 6944

Colors
0592cd
33a6d7
85cae6
1b1b1b

Requirements
Must have
• 1. It must have spot UV on the front of card, maybe back of card too
• 2. I really like the blue on image 6. (or at least a really cool electric blue against the charcoal grey background)
• 3. The font must be slimline and modern. Easy to read
• 4. There must be no black used on the card... Only greys and dark charcoal greys
• 5. Use only the text from the logo "Brackenridge Builders" Not the image of the tree. I am wanting the b-cards to be more masculine.
Nice to have
• 1. I like the design concept on image 6. but happy to see what else you can do with the Spot UV
• 2. Unless you have a really cool idea of the image of the tree (from previous logo) Spot UV somewhere in the design concept thats original and different then I am keen to see what you come up with
• 3. Try changing the color of the logo eg. full white or Blue and white
• 4. Another option is to have the Brackenridge Logo on the front of card with the spot UV in the background of text which we specialise in eg, Roofing, Ceiling, Insulation, Gutter Guards, Electrical, Insurance etc and we can add or reduce items as required. Similar to image 12.
Should not have
• Do not include the image of the tree from previous logo. unless you have a really cool idea of Spot UV somewhere in the design concept thats original and different.

```html
<!DOCTYPE html>
<html lang="en">
<head>
<meta charset="utf-8">
<title>Brackenridge Builders – Business Card</title>
<link rel="stylesheet" href="https://fonts.googleapis.com/css2?family=Montserrat:wght@300;600;700&family=Encode+Sans+Semi+Condensed:wght@400&family=Arimo:wght@400&display=swap">
<style>
  :root {
    --stage-red: #ec3338;
    --card-white: #ffffff;
    --charcoal: #4d4d4d;
    --logo-grey: #4a4b4d;
    --uv-light: #f6f6f7;
    --uv-grey: #ececee;
    --electric-blue: #0a8fcb;
    --mid-blue: #33a6d7;
    --pale-blue: #85cae6;
  }
  * { margin: 0; padding: 0; box-sizing: border-box; }
  html, body { width: 1200px; height: 1200px; overflow: hidden; }
  body { background: var(--stage-red); position: relative; font-family: "Montserrat", sans-serif; }

  .card { position: absolute; left: 180px; width: 840px; height: 480px; overflow: hidden; }
  .card--front { top: 52px; background: var(--card-white); }
  .card--back { top: 668px; background: var(--charcoal); }

  .services-backdrop {
    position: absolute; inset: 0;
    background: linear-gradient(135deg, var(--uv-light) 0%, var(--card-white) 45%, var(--uv-grey) 100%);
  }

  .wordmark { position: absolute; font-family: "Montserrat", sans-serif; line-height: 1; }
  .wordmark__name { display: block; font-weight: 600; letter-spacing: -1.5px; }
  .wordmark__sub { display: block; font-weight: 300; }

  .card--front .wordmark { left: 0; right: 0; top: 200px; text-align: center; color: var(--logo-grey); }
  .card--front .wordmark__name { font-size: 50px; }
  .card--front .wordmark__sub { font-size: 22px; letter-spacing: 33px; margin-top: 12px; padding-left: 33px; }

  .card--back .wordmark { right: 42px; top: 46px; text-align: right; color: var(--electric-blue); }
  .card--back .wordmark__name { font-size: 56px; font-weight: 700; }
  .card--back .wordmark__sub { font-size: 27px; letter-spacing: 40px; margin-top: 14px; margin-right: -40px; }

  .person { position: absolute; left: 0; top: 210px; }
  .person__name {
    font-family: "Arimo", sans-serif; font-weight: 400; font-size: 37px; color: var(--pale-blue);
    padding-left: 31px; width: 342px; border-bottom: 2px solid var(--mid-blue); padding-bottom: 4px; white-space: nowrap;
  }
  .person__title {
    font-family: "Arimo", sans-serif; font-size: 26px; color: var(--mid-blue); margin-top: 6px; padding-left: 108px;
  }

  .contact-list { position: absolute; left: 34px; top: 326px; list-style: none; }
  .contact-list li {
    display: flex; align-items: center; height: 31px;
    font-family: "Encode Sans Semi Condensed", sans-serif; font-size: 20px; color: var(--pale-blue); white-space: nowrap;
  }
  .contact-list .icon { width: 23px; height: 23px; margin-right: 12px; flex: none; }
  .contact-list .label { margin-right: 4px; }
  .contact-list .gap { margin-left: 6px; }
</style>
</head>
<body>

<section class="card card--front" aria-label="Card front">
  <div class="services-backdrop" role="img" aria-label="Spot UV background of the services offered: roofing, ceiling, insulation, gutter guards, electrical, insurance"></div>
  <h1 class="wordmark">
    <span class="wordmark__name">BRACKENRIDGE</span>
    <span class="wordmark__sub">BUILDERS</span>
  </h1>
</section>

<section class="card card--back" aria-label="Card back">
  <div class="wordmark">
    <span class="wordmark__name">BRACKENRIDGE</span>
    <span class="wordmark__sub">BUILDERS</span>
  </div>

  <div class="person">
    <h2 class="person__name">DERMOT QUAILE</h2>
    <p class="person__title">Project Manager</p>
  </div>

  <ul class="contact-list">
    <li>
      <svg class="icon" viewBox="0 0 24 24" aria-hidden="true"><rect width="24" height="24" rx="3" fill="#85cae6"/><path d="M7 5l3 0 1 4-2 1.5c1 2 2.5 3.5 4.5 4.5L15 13l4 1v3c0 1-1 2-2 2C10 19 5 14 5 7c0-1 1-2 2-2z" fill="#4d4d4d"/></svg>
      <span class="label">Mobile :</span> 0412 537 804 <span class="gap label">Office&nbsp; :</span> (08) 9173 5842
    </li>
    <li>
      <svg class="icon" viewBox="0 0 24 24" aria-hidden="true"><rect width="24" height="24" rx="3" fill="#85cae6"/><path d="M12 4l8 7h-2v9H6v-9H4z" fill="#4d4d4d"/><rect x="10" y="14" width="4" height="6" fill="#85cae6"/></svg>
      17C Pellworth Avenue, Malaga WA 6090
    </li>
    <li>
      <svg class="icon" viewBox="0 0 24 24" aria-hidden="true"><rect width="24" height="24" rx="3" fill="#85cae6"/><text x="12" y="17" text-anchor="middle" font-family="Arimo, sans-serif" font-size="15" fill="#4d4d4d">@</text></svg>
      info@brackenridgebuild.com.au
    </li>
    <li>
      <svg class="icon" viewBox="0 0 24 24" aria-hidden="true"><rect width="24" height="24" rx="3" fill="#85cae6"/><rect x="4.5" y="7" width="15" height="11" fill="none" stroke="#4d4d4d" stroke-width="1.6"/><path d="M4.5 11h15M8 11l4 7 4-7" fill="none" stroke="#4d4d4d" stroke-width="1.4"/></svg>
      3817 Malaga WA 6944
    </li>
  </ul>
</section>

</body>
</html>
```